Company Website Re-design for Software development consultancy

We would like our company website to be redesigned using our existing marketing collateral and website content as a guide

current site : www.brackenloft.com.au

For the different pages types and content please base on the following site : https://www.quorvanta.net/

We want a coded site - but will replace the content ourselves within the sections you provide to customise to our needs.

Target Market(s)

Medium to Large corporates needing software design and development services

Industry/Entity Type

Information Technology

Coding

Coded - Design and coding required

Number of Pages Required

5+ page

Font styles to use
Sans Serif

Colors
ec1f27
ffffff
000000

Requirements
Must have
• Align to colour scheme of existing collateral
• Include pages for the key areas of our busines - see : https://www.quorvanta.net/
Nice to have
• image rotators - make the site interesting to the business visitor

```html
<!DOCTYPE html>
<html lang="en">
<head>
<meta charset="utf-8">
<title>Bracken Loft — Software Development Consultancy</title>
<link href="https://fonts.googleapis.com/css2?family=Poppins:wght@400;500;600;700&family=Lato:wght@400;700&display=swap" rel="stylesheet">
<style>
:root{
  --red:#ec1f27;
  --orange:#f2603a;
  --orange-soft:#f47048;
  --white:#ffffff;
  --black:#000000;
  --ink:#1c1c1c;
  --grey:#6f6f6f;
  --grey-light:#9a9a9a;
  --line:#dcdcdc;
  --footer:#1a1a1a;
}
*{box-sizing:border-box;margin:0;padding:0}
html,body{width:1200px;height:4045px;overflow:hidden}
body{position:relative;background:var(--white);font-family:"Lato",Arial,sans-serif;color:var(--ink)}
.section{position:absolute;left:0;width:1200px;overflow:hidden}
.abs{position:absolute}
.heading{font-family:"Poppins",Arial,sans-serif;font-weight:600;font-size:34px;text-align:center;width:100%;letter-spacing:.5px}

/* header */
.site-header{top:0;height:104px;background:var(--white)}
.brand{left:75px;top:34px;font-family:"Poppins",Arial,sans-serif;font-weight:700;font-size:34px;color:var(--black);letter-spacing:.5px;line-height:1}
.main-nav{left:372px;top:42px;display:flex;gap:40px;font-size:14px;color:var(--grey);text-transform:uppercase}
.main-nav .active{color:var(--black)}
.search-icon{left:1098px;top:38px}

/* hero */
.hero{top:104px;height:624px}
.hero-left{left:0;top:0;width:600px;height:624px;background:linear-gradient(135deg,#ee2a2a 0%,var(--red) 50%,#f0452f 100%)}
.hero-photo{left:600px;top:0;width:600px;height:624px;background:linear-gradient(120deg,#8a8f96 0%,#c9ccd0 45%,#e8e8e6 70%,#b9b39f 100%)}
.hero-shade{left:600px;top:0;width:600px;height:624px;background:linear-gradient(90deg,rgba(0,0,0,.35),rgba(0,0,0,.05))}
.hero-mark{left:520px;top:174px;width:155px;height:155px;background:var(--red);border:6px solid var(--white)}
.hero-title{left:710px;top:196px;font-family:"Poppins",Arial,sans-serif;font-weight:700;font-size:42px;color:var(--white);letter-spacing:1px}
.hero-text{left:710px;top:268px;width:430px;font-size:15px;line-height:23px;color:var(--white)}
.hero-btn{left:710px;top:381px;width:188px;height:50px;border-radius:25px;background:var(--red);color:var(--white);font-family:"Poppins",Arial,sans-serif;font-weight:600;font-size:15px;text-align:center;line-height:50px}
.dots{left:712px;top:500px;display:flex;gap:12px}
.dots span{width:14px;height:14px;border-radius:50%;border:2px solid var(--white)}
.dots span.on{background:var(--white)}
.hero-notch{left:480px;top:574px}

/* how it works */
.how{top:728px;height:437px}
.how .heading{top:72px;color:var(--black)}
.step{top:148px;width:340px;text-align:center}
.step-icon{width:135px;height:135px;margin:0 auto;background:var(--red);border-radius:8px;display:flex;align-items:center;justify-content:center}
.step p{margin-top:40px;font-size:20px;line-height:30px;color:var(--black)}
.step em{font-style:normal;color:var(--red)}

/* services */
.services{top:1165px;height:763px;background:linear-gradient(160deg,#16303a 0%,#0d1a22 45%,#112830 100%)}
.services .heading{top:50px;color:var(--white)}
.svc-panel{left:76px;top:151px;width:1048px;height:540px}
.svc-left{left:0;top:0;width:524px;height:540px;background:var(--orange)}
.svc-right{left:524px;top:0;width:524px;height:540px;background:var(--red)}
.svc{color:var(--white)}
.svc h3{font-family:"Poppins",Arial,sans-serif;font-weight:600;font-size:16px;text-transform:uppercase;margin-bottom:6px;white-space:nowrap}
.svc p{font-size:14px;line-height:21px}
.svc-l{left:24px;width:336px;text-align:right}
.svc-r{left:687px;width:340px;text-align:left}
.svc-ring{width:112px;height:112px;border-radius:50%;background:var(--white);border:6px solid rgba(255,255,255,.45);background-clip:padding-box;display:flex;align-items:center;justify-content:center}

/* product */
.product{top:1928px;height:729px}
.product .heading{top:80px;color:var(--black)}
.divider{left:599px;top:150px;height:520px;border-left:2px dashed var(--line)}
.screen{background:linear-gradient(180deg,#3a3d42 0%,#5b5f66 70%,#c7c9cc 100%);border-radius:6px}
.bullet{display:flex;gap:16px;font-size:15px;line-height:22px;color:var(--grey);width:440px}
.bullet svg{flex:none;margin-top:3px}

/* team */
.team{top:2657px;height:499px;background:linear-gradient(90deg,var(--red) 0%,#ef3a30 50%,var(--orange-soft) 100%)}
.team .heading{top:68px;color:var(--white)}
.member{top:148px;width:300px;text-align:center;color:var(--white)}
.avatar{position:relative;width:135px;height:135px;margin:0 auto;border-radius:50%;border:5px solid var(--white);background:linear-gradient(160deg,#b9b3ad,#6d6a68)}
.avatar .badge{position:absolute;right:-10px;bottom:4px;width:40px;height:40px;border-radius:50%;background:var(--white);box-shadow:0 2px 4px rgba(0,0,0,.25)}
.member h4{margin-top:26px;font-family:"Poppins",Arial,sans-serif;font-weight:500;font-size:20px}
.member p{margin-top:6px;font-size:14px;line-height:21px}

/* who we are */
.who{top:3156px;height:458px}
.who .heading{top:58px;color:var(--black)}
.who-text{left:270px;top:125px;width:660px;text-align:center;font-size:15px;line-height:24px;color:var(--grey)}
.client{width:200px;text-align:center;font-family:"Lato",Arial,sans-serif;font-weight:700;font-size:19px;color:#3a3a3a}

/* footer */
.footer{top:3614px;height:364px;background:linear-gradient(180deg,#222 0%,var(--footer) 100%);color:var(--white)}
.footer h5{font-family:"Poppins",Arial,sans-serif;font-weight:600;font-size:17px;text-transform:uppercase;margin-bottom:28px}
.contact-line{display:flex;gap:18px;font-size:14px;line-height:22px;margin-bottom:26px}
.f-nav li{list-style:none;font-size:14px;line-height:24px}
.f-nav li.on{font-weight:700}
.post{display:flex;gap:14px;margin-bottom:20px}
.post-img{width:80px;height:80px;background:linear-gradient(150deg,#6f8fb0,#c8d4e0)}
.post small{display:block;font-size:12px;color:#cfcfcf;margin-bottom:4px}
.post p{font-size:14px;line-height:21px;width:150px}
.news p{font-size:14px;line-height:23px;width:245px}
.news-form{position:relative;margin-top:20px;width:237px;height:42px;border-radius:21px;background:var(--white)}
.news-form span{position:absolute;left:20px;top:12px;font-size:13px;color:var(--grey-light)}
.news-form .send{position:absolute;right:0;top:0;width:62px;height:42px;border-radius:21px;background:var(--red);display:flex;align-items:center;justify-content:center}
.socials{display:flex;gap:12px;margin-top:24px}
.socials span{width:36px;height:36px;border-radius:50%;border:2px solid var(--white)}
.copyright{top:3978px;height:67px;background:linear-gradient(90deg,var(--red),var(--orange));color:var(--white);font-size:13px;text-align:center;line-height:67px}
.copyright b{font-weight:700}
</style>
</head>
<body>

<header class="section site-header">
  <div class="abs brand">BRACKEN LOFT</div>
  <nav class="abs main-nav">
    <span class="active">Home</span><span>Solutions</span><span>Services</span><span>Industries</span><span>Resources</span><span>Clients</span><span>Contact</span>
  </nav>
  <svg class="abs search-icon" width="24" height="24" viewBox="0 0 24 24" fill="none" stroke="#ec1f27" stroke-width="2.4"><circle cx="10" cy="10" r="7"/><line x1="15" y1="15" x2="22" y2="22"/></svg>
</header>

<section class="section hero">
  <div class="abs hero-left"></div>
  <div class="abs hero-photo" role="img" aria-label="Photo of colleagues working together at a laptop in a bright office"></div>
  <div class="abs hero-shade"></div>
  <div class="abs hero-mark"></div>
  <h1 class="abs hero-title">BRACKEN LOFT</h1>
  <p class="abs hero-text">Lorem Ipsum is simply dummy text of the printing and typesetting industry. Lorem Ipsum has been the industry's standard dummy text ever since the 1500s.</p>
  <div class="abs hero-btn">NEED DETAILS..?</div>
  <div class="abs dots"><span class="on"></span><span></span><span></span></div>
  <svg class="abs hero-notch" width="240" height="50" viewBox="0 0 240 50">
    <path d="M0 50 C60 50 70 0 120 0 C170 0 180 50 240 50 Z" fill="#ffffff"/>
    <circle cx="120" cy="26" r="16" fill="none" stroke="#ec1f27" stroke-width="2"/>
    <path d="M120 17 V34 M113 28 L120 35 L127 28" fill="none" stroke="#ec1f27" stroke-width="2.2"/>
  </svg>
</section>

<section class="section how">
  <h2 class="abs heading">HOW IT'S WORK</h2>
  <div class="abs step" style="left:60px">
    <div class="step-icon">
      <svg width="84" height="84" viewBox="0 0 84 84" fill="none" stroke="#fff" stroke-width="3"><circle cx="42" cy="42" r="36"/><circle cx="42" cy="42" r="20"/><ellipse cx="42" cy="42" rx="9" ry="20"/><line x1="22" y1="42" x2="62" y2="42"/><path d="M14 28 l-4 8 8 -2"/><path d="M70 56 l4 -8 -8 2"/></svg>
    </div>
    <p>Create an <em>Account</em></p>
  </div>
  <div class="abs step" style="left:430px">
    <div class="step-icon">
      <svg width="84" height="84" viewBox="0 0 84 84" fill="none" stroke="#fff" stroke-width="3"><circle cx="42" cy="42" r="36"/><path d="M42 20 V50 M30 39 L42 51 L54 39"/><path d="M24 50 V60 H60 V50"/></svg>
    </div>
    <p>Download and install the<br>Lumeno <em>Add-in for Tablix</em></p>
  </div>
  <div class="abs step" style="left:800px">
    <div class="step-icon">
      <svg width="84" height="84" viewBox="0 0 84 84" fill="none" stroke="#fff" stroke-width="3"><circle cx="42" cy="42" r="36"/><path d="M28 56 H24 a10 10 0 0 1 0-20 a14 14 0 0 1 27-4 a11 11 0 0 1 9 24 H56"/><path d="M42 62 V42 M34 49 L42 41 L50 49"/></svg>
    </div>
    <p>Build your models and<br>publish to our <em>Cloud Services</em></p>
  </div>
</section>

<section class="section services" role="region" aria-label="Our services">
  <h2 class="abs heading">OUR SERVICES</h2>
  <div class="abs svc-panel">
    <div class="abs svc-left"></div>
    <div class="abs svc-right"></div>

    <div class="abs svc svc-l" style="top:46px"><h3>Dedicated Development Team</h3><p>Hire a loyal software development team with niche skills and deep expertise.</p></div>
    <div class="abs svc-ring" style="left:380px;top:30px"><svg width="50" height="50" viewBox="0 0 50 50" fill="#222"><circle cx="25" cy="12" r="6"/><circle cx="11" cy="34" r="6"/><circle cx="39" cy="34" r="6"/><path d="M25 20 L13 28 M25 20 L37 28" stroke="#222" stroke-width="2"/></svg></div>

    <div class="abs svc svc-l" style="top:202px"><h3>UI and UX Design</h3><p>Build the product you need on time with an experienced team that uses a clear and effective design process.</p></div>
    <div class="abs svc-ring" style="left:380px;top:187px"><svg width="52" height="46" viewBox="0 0 52 46" fill="none" stroke="#222" stroke-width="2.4"><rect x="3" y="4" width="40" height="28"/><text x="13" y="23" font-family="Lato,Arial,sans-serif" font-size="11" fill="#222" stroke="none">UX</text><path d="M34 28 L46 40 M40 40 H46 V34"/></svg></div>

    <div class="abs svc svc-l" style="top:360px"><h3>QA &amp; Testing</h3><p>Turn to our experts to perform comprehensive, multi-stage testing and auditing of your software.</p></div>
    <div class="abs svc-ring" style="left:380px;top:344px"><svg width="46" height="50" viewBox="0 0 46 50" fill="none" stroke="#222" stroke-width="2.4"><rect x="4" y="4" width="38" height="42"/><path d="M11 14 H35 M11 22 H35 M11 30 H35 M11 38 H25"/></svg></div>

    <div class="abs svc-ring" style="left:556px;top:30px"><svg width="52" height="48" viewBox="0 0 52 48" fill="none" stroke="#222" stroke-width="2.4"><rect x="3" y="6" width="46" height="30"/><path d="M10 28 L20 18 L28 24 L40 12"/><path d="M18 44 H34 M26 36 V44"/></svg></div>
    <div class="abs svc svc-r" style="top:46px"><h3>Enterprise Software Development</h3><p>Create complex enterprise software, ensure reliable software integration, modernise your legacy system.</p></div>

    <div class="abs svc-ring" style="left:556px;top:187px"><svg width="40" height="54" viewBox="0 0 40 54" fill="none" stroke="#222" stroke-width="2.4"><rect x="6" y="3" width="28" height="48" rx="4"/><circle cx="20" cy="27" r="6"/><line x1="15" y1="44" x2="25" y2="44"/></svg></div>
    <div class="abs svc svc-r" style="top:202px"><h3>Mobile App Development</h3><p>Create an impactful mobile app that fits your brand and industry within a shorter time frame.</p></div>

    <div class="abs svc-ring" style="left:556px;top:344px"><svg width="54" height="48" viewBox="0 0 54 48" fill="#222"><circle cx="27" cy="10" r="6"/><circle cx="10" cy="24" r="5"/><circle cx="44" cy="24" r="5"/><rect x="16" y="30" width="22" height="14"/><rect x="3" y="34" width="12" height="10"/><rect x="39" y="34" width="12" height="10"/></svg></div>
    <div class="abs svc svc-r" style="top:360px"><h3>IT Consulting</h3><p>Trust our top minds to eliminate workflow pain points, implement new tech, and consolidate app portfolios.</p></div>
  </div>
</section>

<section class="section product">
  <h2 class="abs heading">Lumeno PRODUCT INFO</h2>
  <div class="abs divider"></div>
  <div class="abs screen" style="left:189px;top:149px;width:337px;height:323px" role="img" aria-label="Desktop monitor showing the Lumeno web dashboard"></div>
  <div class="abs screen" style="left:674px;top:149px;width:383px;height:323px" role="img" aria-label="Desktop monitor showing a spreadsheet tax calculation model"></div>

  <div class="abs bullet" style="left:86px;top:528px"><svg width="20" height="20" viewBox="0 0 20 20" fill="#ec1f27"><rect x="7" y="0" width="6" height="6"/><rect x="0" y="7" width="6" height="6"/><rect x="14" y="7" width="6" height="6"/><rect x="7" y="14" width="6" height="6"/></svg><span>Publish with one-click using our Tablix Add-in.</span></div>
  <div class="abs bullet" style="left:86px;top:596px"><svg width="20" height="20" viewBox="0 0 20 20" fill="#ec1f27"><rect x="7" y="0" width="6" height="6"/><rect x="0" y="7" width="6" height="6"/><rect x="14" y="7" width="6" height="6"/><rect x="7" y="14" width="6" height="6"/></svg><span>Calculation logic in Tablix is automatically converted into an industry-standard web service.</span></div>
  <div class="abs bullet" style="left:636px;top:524px;width:460px"><svg width="20" height="20" viewBox="0 0 20 20" fill="#ec1f27"><rect x="7" y="0" width="6" height="6"/><rect x="0" y="7" width="6" height="6"/><rect x="14" y="7" width="6" height="6"/><rect x="7" y="14" width="6" height="6"/></svg><span>Manage subscriptions to your models via an interactive web portal.</span></div>
  <div class="abs bullet" style="left:636px;top:596px;width:460px"><svg width="20" height="20" viewBox="0 0 20 20" fill="#ec1f27"><rect x="7" y="0" width="6" height="6"/><rect x="0" y="7" width="6" height="6"/><rect x="14" y="7" width="6" height="6"/><rect x="7" y="14" width="6" height="6"/></svg><span>Track usage of your models and associate with a pricing model.</span></div>
</section>

<section class="section team">
  <h2 class="abs heading">MEET OUR TEAM</h2>
  <div class="abs member" style="left:100px">
    <div class="avatar" role="img" aria-label="Portrait photo of Miles Hartwell"><span class="badge"></span></div>
    <h4>Miles Hartwell</h4>
    <p>Miles's one of the best developers<br>on the planet</p>
  </div>
  <div class="abs member" style="left:450px">
    <div class="avatar" role="img" aria-label="Portrait photo of Owen Pryce"><span class="badge"></span></div>
    <h4>Owen Pryce</h4>
    <p>Owen's been running software<br>projects for 20 years</p>
  </div>
  <div class="abs member" style="left:795px">
    <div class="avatar" role="img" aria-label="Portrait photo of Grant Tilley"><span class="badge"></span></div>
    <h4>Grant Tilley</h4>
    <p>Grant codes for fun as much<br>as he does for work</p>
  </div>
  <svg class="abs" style="left:480px;top:449px" width="240" height="50" viewBox="0 0 240 50"><path d="M0 50 C60 50 70 0 120 0 C170 0 180 50 240 50 Z" fill="#ffffff"/></svg>
</section>

<section class="section who">
  <h2 class="abs heading">WHO WE ARE</h2>
  <p class="abs who-text">Lorem Ipsum is simply dummy text of the printing and typesetting industry. Lorem Ipsum has been the industry's standard dummy text ever since the 1500s.</p>
  <div class="abs client" style="left:62px;top:243px">Ridgeway Motors</div>
  <div class="abs client" style="left:278px;top:243px">Halcyon Pictures</div>
  <div class="abs client" style="left:500px;top:243px">CareWell</div>
  <div class="abs client" style="left:723px;top:243px">Dunmore</div>
  <div class="abs client" style="left:938px;top:243px">Norvane</div>
  <div class="abs client" style="left:62px;top:331px">Ironpeak</div>
  <div class="abs client" style="left:278px;top:331px">Velmora</div>
  <div class="abs client" style="left:500px;top:331px">Clarisse</div>
  <div class="abs client" style="left:723px;top:331px">Quattor</div>
  <div class="abs client" style="left:938px;top:331px">Railstar</div>
</section>

<footer class="section footer">
  <div class="abs" style="left:76px;top:52px">
    <h5>Get in Touch</h5>
    <div class="contact-line"><svg width="16" height="20" viewBox="0 0 16 20" fill="#ec1f27"><path d="M8 0 a8 8 0 0 1 8 8 c0 6 -8 12 -8 12 s-8 -6 -8 -12 a8 8 0 0 1 8 -8z"/><circle cx="8" cy="8" r="3" fill="#1a1a1a"/></svg><span>42 Harbour Lane,<br>Sydney 2000</span></div>
    <div class="contact-line"><svg width="16" height="18" viewBox="0 0 16 18" fill="#ec1f27"><path d="M3 0 L7 4 L5 7 C6 10 8 12 11 13 L14 11 L16 15 L13 18 C6 17 0 11 0 4 Z"/></svg><span>555-010-2040</span></div>
    <div class="contact-line"><svg width="18" height="14" viewBox="0 0 18 14" fill="#ec1f27"><rect width="18" height="14" rx="1"/><path d="M1 1 L9 8 L17 1" fill="none" stroke="#1a1a1a" stroke-width="1.6"/></svg><span>info@brackenloft.com.au</span></div>
  </div>
  <div class="abs" style="left:345px;top:52px">
    <h5>Navigation</h5>
    <ul class="f-nav"><li class="on">- Home</li><li>- Solution</li><li>- Services</li><li>- Industries</li><li>- Resources</li><li>- Clients</li><li>- Contact</li></ul>
  </div>
  <div class="abs" style="left:561px;top:52px">
    <h5>Blog Updates</h5>
    <div class="post"><div class="post-img" role="img" aria-label="Blog thumbnail photo of a team meeting"></div><div><small>Posted 17/09/2018</small><p>Lorem Ipsum is simply Ipsum is simply dummy</p></div></div>
    <div class="post"><div class="post-img" role="img" aria-label="Blog thumbnail photo of a team meeting"></div><div><small>Posted 17/09/2018</small><p>Lorem Ipsum is simply Ipsum is simply dummy</p></div></div>
  </div>
  <div class="abs news" style="left:885px;top:52px">
    <h5>Newslatter</h5>
    <p>Would you like to receive exclusive access to articles, white papers and our regular monthly newsletter?</p>
    <div class="news-form"><span>Email</span><div class="send"><svg width="20" height="20" viewBox="0 0 20 20" fill="#fff"><path d="M0 8 L20 0 L13 20 L10 11 Z"/></svg></div></div>
    <div class="socials"><span></span><span></span><span></span><span></span></div>
  </div>
</footer>

<div class="section copyright">Copyright © <b>BRACKEN LOFT</b> - 2018 , All Right Reserved</div>

</body>
</html>
```